"Lanterns Along Every Quiet Road" Sermon Series Design

Needing a design for our church's next sermon series titled "Lanterns Along Every Quiet Road" where we will discuss the need for unity, diversity, love and clarity. Looking for a 1920 x 1080 (or higher res) editable and layered file (PSD or AI) so that we can reformat the design to work on social, screens, lower thirds and various print and online mediums. We will also need to have access to the font files so that we can make resize and tweak as needed. We like the idea of using a globe or map of the world as the backdrop with the words overtop. Or, the idea of creating a bunch of newspaper clippings (generic, so that they can't actually be read) and making the shape of a heart. See attached examples. This website will give you an idea of our previous sermon series designs so you can have an idea of our style (but, feel free to help us advance the ball on something more aligned with current design trends): https://www.brambleford.example/series

Examples use red, but stay away from a ton of red. If you're gonna major in a color, use blue or something in that family.

Must haves:
Title: Lanterns Along Every Quiet Road
Tagline : (TBD - use some Lorem Ipsum as a placeholder and we will fill in later)
Our Logo (attached) (small towards bottom is standard - only use solid colors for logo - preferably just solid black or white)

Industry/Entity Type

Church

Font styles to use
Serif
Sans Serif

Requirements
Must have
• Title: Lanterns Along Every Quiet Road
Nice to have
• We like the idea of using a globe or map of the world as the backdrop with the words overtop. Or, the idea of creating a bunch of newspaper clippings (generic, so that they can't actually be read) and making the shape of a heart. See attached examples.

If you're gonna major on a color, stick with blue or something close.
Should not have
• Don't use red as the primary color (example we sent has red, but stay away from it)

```html
<!DOCTYPE html>
<html lang="en">
<head>
<meta charset="utf-8">
<title>Lanterns Along Every Quiet Road — Sermon Series</title>
<link rel="stylesheet" href="https://fonts.googleapis.com/css2?family=Montserrat:wght@800;900&family=Montserrat+Alternates:wght@400&display=swap">
<style>
  :root {
    --navy-deep: #061a63;
    --navy: #0a2a8a;
    --royal: #0346b0;
    --azure: #0560c9;
    --land: rgba(3, 20, 90, 0.45);
    --band: rgba(255, 255, 255, 0.05);
    --ink: #ffffff;
  }
  * { margin: 0; padding: 0; box-sizing: border-box; }
  html, body { width: 1200px; height: 675px; overflow: hidden; background: var(--navy-deep); }
  .series-slide {
    position: relative;
    width: 1200px;
    height: 675px;
    overflow: hidden;
    background: linear-gradient(215deg, var(--azure) 0%, var(--royal) 35%, var(--navy) 70%, var(--navy-deep) 100%);
    font-family: "Montserrat", Arial, sans-serif;
    color: var(--ink);
  }
  .light-bands { position: absolute; inset: 0; width: 100%; height: 100%; }
  .world-map {
    position: absolute;
    left: 12px; top: 50px;
    width: 1176px; height: 580px;
    border-radius: 40% 45% 38% 42%;
    background: radial-gradient(ellipse at 50% 45%, var(--land) 0%, rgba(3, 20, 90, 0.25) 55%, rgba(3, 20, 90, 0) 75%);
  }
  .series-title {
    position: absolute;
    left: 0; right: 0; top: 205px;
    text-align: center;
    font-weight: 900;
    text-transform: uppercase;
    line-height: 1;
  }
  .series-title .line-one { display: block; font-size: 68px; letter-spacing: -1px; }
  .series-title .line-two { display: block; font-size: 66px; letter-spacing: -1px; margin-top: 10px; }
  .tagline {
    position: absolute;
    left: 0; right: 0; top: 428px;
    text-align: center;
    font-family: "Montserrat Alternates", Arial, sans-serif;
    font-weight: 400;
    font-size: 25px;
    letter-spacing: 0.2em;
  }
  .church-mark {
    position: absolute;
    left: 0; right: 0; top: 574px;
    display: flex;
    align-items: center;
    justify-content: center;
    gap: 10px;
  }
  .church-mark .dot {
    width: 22px; height: 22px;
    border: 2.5px solid var(--ink);
    border-radius: 50%;
  }
  .church-mark .name {
    font-family: "Montserrat", Arial, sans-serif;
    font-weight: 800;
    font-size: 16px;
    letter-spacing: 0.12em;
    text-transform: uppercase;
  }
</style>
</head>
<body>
  <main class="series-slide">
    <div class="world-map" role="img" aria-label="Faint world map backdrop showing the continents"></div>
    <svg class="light-bands" viewBox="0 0 1200 675" aria-hidden="true">
      <polygon points="0,330 560,0 700,0 0,410" fill="var(--band)"/>
      <polygon points="300,675 1200,150 1200,260 480,675" fill="var(--band)"/>
      <polygon points="700,675 1200,380 1200,460 840,675" fill="var(--band)"/>
      <polygon points="820,0 1200,0 1200,40 760,300 600,300" fill="rgba(255,255,255,0.04)"/>
    </svg>
    <h1 class="series-title">
      <span class="line-one">Lanterns Along</span>
      <span class="line-two">Every Quiet Road</span>
    </h1>
    <p class="tagline">Lorem ipsum dolor sit amet</p>
    <div class="church-mark">
      <span class="dot"></span>
      <span class="name">Brambleford</span>
    </div>
  </main>
</body>
</html>
```